Business Card for Wellness Clinic

We need a business card for our new logo. I want it to match the feel of the logo

Target Market(s)

Young professional families looking for holistic health care

Industry/Entity Type

Health And Wellness

Contact Information for Business Card

Our business Name: Brackenfield Health & wellness Centre, our phone #, email address...see attached old business card

Font styles to use
Sans Serif

Colors
33b8a4
cee9f5

Requirements
Must have
• my logo and business name
• Font is "Helvetica Neue LT Std 45 Light" and
• Only for "&" using font "Trajan pro bold"
• Use colors in the logo

```html
<!DOCTYPE html>
<html lang="en">
<head>
<meta charset="utf-8">
<title>Brackenfield Health &amp; wellness Centre – Business Card</title>
<link href="https://fonts.googleapis.com/css2?family=Oswald:wght@300;400&display=swap" rel="stylesheet">
<style>
  :root {
    --teal: #0fb39f;
    --teal-text: #12b8a3;
    --ink: #231f20;
    --logo-grey: #d9d9d9;
    --page: #e9ecec;
    --white: #ffffff;
  }
  * { box-sizing: border-box; margin: 0; padding: 0; }
  html, body { width: 1200px; height: 900px; overflow: hidden; }
  body {
    background: var(--page);
    font-family: "Oswald", "Helvetica Neue", Arial, sans-serif;
    font-weight: 300;
    position: relative;
  }
  .card {
    position: absolute;
    left: 250px;
    width: 700px;
    height: 400px;
    overflow: hidden;
    box-shadow: 0 6px 18px rgba(0,0,0,0.18);
  }
  .card--appointment { top: 36px; background: var(--ink); }
  .card--contact { top: 464px; background: var(--teal); }
  .card svg.shapes { position: absolute; inset: 0; }

  .brand {
    position: absolute;
    text-align: center;
    color: var(--logo-grey);
    font-weight: 300;
    text-transform: uppercase;
    letter-spacing: 0.28em;
    font-size: 15px;
    line-height: 1.45;
  }
  .brand__mark {
    display: block;
    width: 34px;
    height: 34px;
    background: var(--teal);
    margin: 0 auto 10px;
  }

  /* appointment side */
  .card--appointment .brand { left: 0; right: 0; top: 26px; }
  .appt-field {
    position: absolute;
    left: 60px;
    color: var(--teal-text);
    font-size: 24px;
    font-weight: 300;
    line-height: 1;
  }
  .appt-field--date { top: 150px; }
  .appt-field--for { top: 186px; }
  .appt-at {
    position: absolute;
    left: 495px;
    top: 152px;
    color: var(--teal-text);
    font-size: 18px;
  }
  .appt-notice {
    position: absolute;
    left: 0; right: 0;
    top: 272px;
    text-align: center;
    color: var(--ink);
    font-size: 21px;
    font-style: italic;
    line-height: 1.4;
    font-weight: 300;
  }

  /* contact side */
  .card--contact .brand { left: 14px; width: 240px; top: 110px; font-size: 13px; }
  .address {
    position: absolute;
    left: 18px;
    width: 192px;
    top: 318px;
    text-align: center;
    color: var(--teal-text);
    font-size: 15px;
    line-height: 1.5;
    letter-spacing: -0.01em;
    white-space: nowrap;
  }
  .person__name {
    position: absolute;
    left: 282px;
    top: 60px;
    color: var(--white);
    font-size: 30px;
    font-weight: 400;
    line-height: 1;
    letter-spacing: -0.01em;
  }
  .person__title {
    position: absolute;
    left: 282px;
    top: 100px;
    color: var(--ink);
    font-size: 20px;
    line-height: 1;
  }
  .contact-list { position: absolute; left: 278px; top: 232px; list-style: none; }
  .contact-list li {
    display: flex;
    align-items: center;
    gap: 14px;
    height: 46px;
    color: var(--ink);
    font-size: 23px;
    letter-spacing: -0.01em;
  }
  .contact-list svg { width: 32px; height: 32px; flex: none; }
</style>
</head>
<body>

<section class="card card--appointment" aria-label="Appointment card">
  <svg class="shapes" viewBox="0 0 700 400" aria-hidden="true">
    <rect x="0" y="262" width="700" height="138" fill="var(--teal)"/>
    <line x1="106" y1="172" x2="485" y2="172" stroke="var(--teal)" stroke-width="1.5"/>
    <line x1="520" y1="172" x2="650" y2="172" stroke="var(--teal)" stroke-width="1.5"/>
    <line x1="98" y1="208" x2="650" y2="208" stroke="var(--teal)" stroke-width="1.5"/>
  </svg>
  <div class="brand">
    <span class="brand__mark"></span>
    Brackenfield Health<br>&amp; wellness Centre
  </div>
  <span class="appt-field appt-field--date">date</span>
  <span class="appt-at">@</span>
  <span class="appt-field appt-field--for">for</span>
  <p class="appt-notice">If you are unable to keep your appointment, please provide<br>at least 2 business days notice or full visit fees will apply.</p>
</section>

<section class="card card--contact" aria-label="Contact card">
  <svg class="shapes" viewBox="0 0 700 400" aria-hidden="true">
    <path d="M0 0 H268 V92 H700 V55 H268 V0 Z" fill="var(--ink)"/>
    <path d="M0 0 H268 C300 140 290 300 200 400 H0 Z" fill="var(--ink)"/>
    <path d="M222 0 H240 C262 110 260 230 236 290 C248 200 246 100 222 0 Z" fill="var(--teal)"/>
  </svg>
  <div class="brand">
    <span class="brand__mark"></span>
    Brackenfield Health<br>&amp; wellness Centre
  </div>
  <p class="address">412 Alder St. West, Suite 305<br>Ottawa, ON K1R 2B7</p>
  <h1 class="person__name">DR. MAREN HOLLOWAY, N.D.</h1>
  <p class="person__title">NATUROPATHIC DOCTOR</p>
  <ul class="contact-list">
    <li>
      <svg viewBox="0 0 32 32" aria-hidden="true"><circle cx="16" cy="16" r="16" fill="var(--ink)"/><path d="M11 8.5c1-.6 2-.3 2.4.6l1.2 2.6c.3.7.1 1.4-.5 1.9l-1 .8c.8 2 2.4 3.6 4.4 4.5l.8-1c.5-.6 1.3-.8 2-.5l2.5 1.2c.9.4 1.2 1.4.6 2.3-1 1.6-2.6 2.4-4.5 1.8-4.5-1.5-8-5-9.4-9.4-.5-1.8.3-3.600 1.5-4.8z" fill="var(--teal)"/></svg>
      613-555-0148
    </li>
    <li>
      <svg viewBox="0 0 32 32" aria-hidden="true"><circle cx="16" cy="16" r="16" fill="var(--ink)"/><g fill="none" stroke="var(--teal)" stroke-width="1.6"><circle cx="16" cy="16" r="8.5"/><ellipse cx="16" cy="16" rx="3.8" ry="8.5"/><line x1="7.5" y1="16" x2="24.5" y2="16"/><line x1="9" y1="11.5" x2="23" y2="11.5"/><line x1="9" y1="20.5" x2="23" y2="20.5"/></g></svg>
      www.brackenfieldnd.ca
    </li>
    <li>
      <svg viewBox="0 0 32 32" aria-hidden="true"><circle cx="16" cy="16" r="16" fill="var(--ink)"/><rect x="8" y="10.5" width="16" height="11" fill="none" stroke="var(--teal)" stroke-width="1.6"/><path d="M8 10.5 L16 17 L24 10.5" fill="none" stroke="var(--teal)" stroke-width="1.6"/></svg>
      mholloway@brackenfieldnd.ca
    </li>
  </ul>
</section>

</body>
</html>
```